Social Media Monitoring Web Site Design

We need a responsive web design for a new company based in Ireland. We offer a social media monitoring service that works in a call centre environment. Our service name is 'TROVA'. We have a logo that is attached.

Sites we like (in no particular order):

1. http://www.lumengrove.com/
2. https://quillnest.io/
3. https://www.markoriel.com/

We want the web site to have the following sections:

HOME
TROVA PLATFORM
TROVA SERVICE
CASE STUDIES
ABOUT US
CONTACT US

We also need a customer Login link. The site must be a responsive design.

Target Market(s)

Corporate Customers

Industry/Entity Type

It Company

Coding

Coded - Design and coding required

Number of Pages Required

2 page

Requirements
Must have
• Responsive Design
• Bootstrap
Nice to have
• Animations

```html
<!DOCTYPE html>
<html lang="en">
<head>
<meta charset="utf-8">
<title>TROVA – Social Monitoring for the New Age</title>
<link rel="stylesheet" href="https://fonts.googleapis.com/css2?family=Saira+Condensed:wght@400;500;600&family=Fira+Sans:wght@400;500;600&display=swap">
<style>
  :root {
    --blue: #1b9be0;
    --blue-dark: #1187cc;
    --orange: #f07a22;
    --ink: #4a4a4a;
    --ink-soft: #5c5c5c;
    --hero-bg-top: #f4f5f7;
    --hero-bg-bottom: #e6e8eb;
    --band-grey: #6b6b6b;
    --white: #ffffff;
  }
  * { box-sizing: border-box; margin: 0; padding: 0; }
  html, body { width: 1200px; height: 2441px; overflow: hidden; }
  body {
    position: relative;
    background: var(--white);
    font-family: "Fira Sans", Arial, sans-serif;
    color: var(--ink);
  }
  .display { font-family: "Saira Condensed", "Arial Narrow", sans-serif; }

  /* Hero */
  .hero {
    position: absolute; left: 0; top: 0; width: 1200px; height: 789px;
    background: linear-gradient(180deg, var(--hero-bg-top), var(--hero-bg-bottom));
  }
  .top-actions { position: absolute; top: 0; left: 789px; display: flex; gap: 12px; }
  .top-actions a {
    display: flex; align-items: center; justify-content: center; gap: 8px;
    height: 33px; color: var(--white); text-decoration: none;
    font-weight: 600; font-size: 17px; border-radius: 0 0 4px 4px;
  }
  .btn-try { width: 183px; background: var(--orange); }
  .btn-login { width: 160px; background: var(--blue); }

  .brand {
    position: absolute; display: flex; align-items: center; gap: 14px;
    font-family: "Saira Condensed", sans-serif; font-weight: 500;
    color: var(--ink-soft); letter-spacing: 4px;
  }
  .brand .mark { background: var(--orange); }
  .brand-header { left: 62px; top: 78px; font-size: 56px; }
  .brand-header .mark { width: 34px; height: 34px; }

  .main-nav {
    position: absolute; top: 96px; left: 470px; display: flex; gap: 22px;
    font-family: "Saira Condensed", sans-serif; font-size: 24px; font-weight: 500;
  }
  .main-nav a { color: var(--ink-soft); text-decoration: none; text-transform: uppercase; padding: 2px 6px; }
  .main-nav a.current { background: var(--blue); color: var(--white); }

  .hero-visual {
    position: absolute; left: 228px; top: 234px; width: 744px; height: 396px;
    border-radius: 16px 16px 4px 4px;
    background: linear-gradient(135deg, #9aa6b4 0%, #d7dde4 45%, #7a8694 100%);
  }
  .hero-title {
    position: absolute; top: 642px; left: 0; width: 1200px; text-align: center;
    font-family: "Saira Condensed", sans-serif; font-weight: 500; color: var(--ink-soft);
    font-size: 56px; letter-spacing: 1px; text-transform: uppercase;
  }
  .hero-title small { font-size: 40px; }
  .hero-sub {
    position: absolute; top: 714px; left: 0; width: 1200px; text-align: center;
    color: var(--blue); font-size: 28px; font-weight: 500;
  }

  /* Intro band */
  .intro {
    position: absolute; left: 0; top: 789px; width: 1200px; height: 328px;
    background: var(--blue); text-align: center; color: var(--white);
  }
  .intro h2 {
    margin-top: 36px; font-family: "Saira Condensed", sans-serif; font-weight: 500;
    font-size: 60px; text-transform: uppercase; line-height: 1;
  }
  .intro p { margin-top: 30px; font-size: 27px; font-weight: 500; line-height: 1.35; }
  .btn-orange {
    display: inline-block; margin-top: 24px; width: 226px; height: 43px; line-height: 43px;
    background: var(--orange); color: var(--white); font-size: 26px; font-weight: 600; text-decoration: none;
  }

  .round-arrow { position: absolute; left: 567px; width: 66px; height: 66px; }

  /* Features */
  .features { position: absolute; left: 0; top: 1170px; width: 1200px; }
  .features h2 {
    text-align: center; color: var(--blue); font-family: "Saira Condensed", sans-serif;
    font-weight: 500; font-size: 56px; line-height: 1; text-transform: uppercase;
  }
  .features .lead { text-align: center; margin-top: 14px; font-size: 26px; font-weight: 600; color: var(--ink); }
  .feature { position: absolute; width: 440px; }
  .feature svg { position: absolute; left: -86px; top: 0; width: 66px; height: 60px; }
  .feature h3 {
    color: var(--blue); font-family: "Saira Condensed", sans-serif; font-weight: 500;
    font-size: 30px; line-height: 1; text-transform: uppercase;
  }
  .feature p { margin-top: 6px; font-size: 16px; font-weight: 500; line-height: 1.3; color: var(--ink); }
  .btn-outline {
    position: absolute; display: flex; align-items: center; justify-content: center;
    left: 435px; width: 328px; height: 60px; border-radius: 12px;
    font-size: 24px; font-weight: 600; text-decoration: none;
  }
  .btn-discover { top: 1654px; border: 3px solid var(--ink-soft); color: var(--ink); background: var(--white); }

  /* Testimonials band */
  .testimonials {
    position: absolute; left: 0; top: 1762px; width: 1200px; height: 297px;
    background: linear-gradient(90deg, #5d5d5b, #767674 50%, #5a5a58); text-align: center; color: var(--white);
  }
  .testimonials h2 {
    margin-top: 32px; font-family: "Saira Condensed", sans-serif; font-weight: 500;
    font-size: 56px; line-height: 1; text-transform: uppercase;
  }
  .testimonials p { margin-top: 6px; font-size: 26px; font-weight: 600; }
  .btn-testimonials { top: 168px; border: 3px solid var(--blue); color: var(--blue); background: var(--white); }

  /* Footer */
  .footer-nav {
    position: absolute; top: 2126px; left: 0; width: 1200px; display: flex; justify-content: center; gap: 20px;
    font-family: "Saira Condensed", sans-serif; font-size: 22px; font-weight: 500;
  }
  .footer-nav a { color: var(--ink-soft); text-decoration: none; text-transform: uppercase; padding: 0 6px; }
  .footer-nav a.current { background: var(--blue); color: var(--white); }
  .brand-footer { left: 462px; top: 2186px; font-size: 52px; }
  .brand-footer .mark { width: 30px; height: 30px; }
  .contact {
    position: absolute; top: 2266px; left: 0; width: 1200px; display: flex; justify-content: center; gap: 40px;
    font-size: 26px; font-weight: 500; color: var(--ink);
  }
  .contact span { display: flex; align-items: center; gap: 12px; }
  .contact svg { width: 34px; height: 26px; }
</style>
</head>
<body>

<header class="hero">
  <nav class="top-actions">
    <a class="btn-try" href="#">
      <svg width="20" height="20" viewBox="0 0 20 20"><circle cx="10" cy="10" r="8" fill="none" stroke="#fff" stroke-width="2.5"/><path d="M10 5v5l3 2" stroke="#fff" stroke-width="2.5" fill="none"/></svg>
      Try it Out
    </a>
    <a class="btn-login" href="#">
      <svg width="16" height="20" viewBox="0 0 16 20"><rect x="1" y="8" width="14" height="11" rx="1" fill="#fff"/><path d="M4 8V5a4 4 0 0 1 8 0v3" stroke="#fff" stroke-width="2.5" fill="none"/></svg>
      Login
    </a>
  </nav>

  <div class="brand brand-header"><span class="mark"></span>TROVA</div>

  <nav class="main-nav">
    <a class="current" href="#">Home</a>
    <a href="#">Trova Platform</a>
    <a href="#">Trova Service</a>
    <a href="#">Case Studies</a>
    <a href="#">About Us</a>
    <a href="#">Contact Us</a>
  </nav>

  <div class="hero-visual" role="img" aria-label="Laptop showing a hand touching a network of connected social profile icons"></div>

  <h1 class="hero-title">Social Monitoring <small>for the new age</small></h1>
  <p class="hero-sub">Giving you the Social Power</p>
</header>

<section class="intro" role="region" aria-label="Introduction">
  <h2>Never miss a thing online</h2>
  <p>Listen to what's being said on the web and social web.<br>React quickly, collaborate, and analyze your online presence.</p>
  <a class="btn-orange" href="#">Learn More</a>
</section>

<svg class="round-arrow" style="top:1098px" viewBox="0 0 66 66" aria-hidden="true">
  <circle cx="33" cy="33" r="31" fill="#fff"/>
  <circle cx="33" cy="33" r="24" fill="none" stroke="#1b9be0" stroke-width="3"/>
  <path d="M24 26l9 8 9-8M24 34l9 8 9-8" fill="none" stroke="#1b9be0" stroke-width="3"/>
</svg>

<section class="features">
  <h2>Features</h2>
  <p class="lead">Discover what Trova can do for you?</p>
</section>

<div class="feature" style="left:173px;top:1330px">
  <svg viewBox="0 0 66 60" aria-hidden="true"><circle cx="33" cy="30" r="22" fill="none" stroke="#4a4a4a" stroke-width="5"/><circle cx="33" cy="30" r="10" fill="#4a4a4a"/><rect x="4" y="22" width="8" height="18" rx="3" fill="#4a4a4a"/><rect x="54" y="22" width="8" height="18" rx="3" fill="#4a4a4a"/></svg>
  <h3>Monitor in real-time</h3>
  <p>Monitor millions of sources in 42 languages<br>and make sure you're not missing anything<br>published on the web and social networks.</p>
</div>

<div class="feature" style="left:736px;top:1330px">
  <svg viewBox="0 0 66 60" aria-hidden="true"><path d="M8 30a22 22 0 0 0 40 14z" fill="#4a4a4a"/><path d="M44 10l4-8M52 18l9-4M54 28h9" stroke="#4a4a4a" stroke-width="4"/></svg>
  <h3>React in seconds</h3>
  <p>Connect your social accounts<br>(Chirper, Friendbook, Queuely) to your alerts<br>and react without leaving the application.</p>
</div>

<div class="feature" style="left:173px;top:1492px">
  <svg viewBox="0 0 66 60" aria-hidden="true"><rect x="4" y="6" width="58" height="40" fill="none" stroke="#4a4a4a" stroke-width="4"/><path d="M12 36l12-12 8 8 18-16" fill="none" stroke="#4a4a4a" stroke-width="3"/><rect x="24" y="48" width="18" height="5" fill="#4a4a4a"/></svg>
  <h3>Analyze and share statistics and reports</h3>
  <p>Get a snapshot of your mentions by source,<br>language, and over a selected period of time.<br>Generate reports and export data to compare<br>yourself with your competitors.</p>
</div>

<div class="feature" style="left:736px;top:1492px">
  <svg viewBox="0 0 66 60" aria-hidden="true"><circle cx="18" cy="8" r="6" fill="#4a4a4a"/><circle cx="48" cy="8" r="6" fill="#4a4a4a"/><path d="M10 16h16v22h-4v20h-8V38h-4zM40 16h16v22h-4v20h-8V38h-4z" fill="#4a4a4a"/><path d="M26 22l7 6 7-6" stroke="#4a4a4a" stroke-width="3" fill="none"/></svg>
  <h3>Work smartly and quickly as a team</h3>
  <p>Build your team, share your alerts, and<br>assign tasks to the right person for the<br>job.</p>
</div>

<a class="btn-outline btn-discover" href="#">Discover Our Features</a>

<section class="testimonials" role="img" aria-label="Overhead view of a busy office desk with laptops and papers, darkened behind text">
  <h2>Listen to what they say about us</h2>
  <p>Hear why people choose Trova....</p>
  <a class="btn-outline btn-testimonials" href="#">Testimonials</a>
</section>

<svg class="round-arrow" style="top:2026px" viewBox="0 0 66 66" aria-hidden="true">
  <circle cx="33" cy="33" r="31" fill="#fff"/>
  <circle cx="33" cy="33" r="24" fill="none" stroke="#4a4a4a" stroke-width="3"/>
  <path d="M24 40l9-8 9 8M24 32l9-8 9 8" fill="none" stroke="#4a4a4a" stroke-width="3"/>
</svg>

<footer>
  <nav class="footer-nav">
    <a class="current" href="#">Home</a>
    <a href="#">Trova Platform</a>
    <a href="#">Trova Service</a>
    <a href="#">Case Studies</a>
    <a href="#">About Us</a>
    <a href="#">Contact Us</a>
  </nav>
  <div class="brand brand-footer"><span class="mark"></span>TROVA</div>
  <div class="contact">
    <span>
      <svg viewBox="0 0 34 26" aria-hidden="true"><path d="M2 10c0-6 30-6 30 0v3h-8v-4c-4-2-10-2-14 0v4H2z" fill="#1b9be0"/><rect x="8" y="14" width="18" height="10" rx="3" fill="#1b9be0"/></svg>
      353-210 (5678)
    </span>
    <span>
      <svg viewBox="0 0 34 26" aria-hidden="true"><rect x="2" y="3" width="30" height="20" fill="#1b9be0"/><path d="M2 3l15 12 15-12" fill="none" stroke="#fff" stroke-width="2.5"/></svg>
      info@trova.io
    </span>
  </div>
</footer>

</body>
</html>
```